Oven Cleaning Business owner needs business card design

Hi there,
Would like for a business card to be designed for myself, the owner of a professional oven cleaning business on the Sunshine Coast.
Would like it to look sleek, and modern-ish. Bit creative is encouraged too.
Include following:
Name/title: Corin ter Haghe, Owner
Phone number: 1300 482 916
Email: info@hearthshinecrew.com.au
Website: www.hearthshinecrew.com.au

```html
<!DOCTYPE html>
<html lang="en">
<head>
<meta charset="utf-8">
<title>Hearthshine Crew – Business Card</title>
<link rel="stylesheet" href="https://fonts.googleapis.com/css2?family=Montserrat:wght@700&family=Arimo:wght@400&display=swap">
<style>
  :root {
    --stage: #c9c9c9;
    --ink: #1f1f20;
    --ink-deep: #161617;
    --paper: #ffffff;
    --teal: #4fc0cc;
    --text-light: #f2f2f2;
  }
  * { margin: 0; padding: 0; box-sizing: border-box; }
  html, body { width: 1200px; height: 788px; overflow: hidden; }
  body {
    background: var(--stage);
    position: relative;
    font-family: "Arimo", Arial, sans-serif;
  }
  .card {
    position: absolute;
    width: 540px;
    height: 309px;
    border-radius: 22px;
    overflow: hidden;
    box-shadow: 0 10px 28px rgba(0,0,0,.25);
  }
  .card-front { left: 30px; top: 240px; background: var(--ink); }
  .card-back { left: 630px; top: 240px; background: var(--ink-deep); }

  .front-shape { position: absolute; inset: 0; width: 100%; height: 100%; }

  .brand {
    position: absolute;
    display: flex;
    align-items: center;
    gap: 12px;
    font-family: "Montserrat", Arial, sans-serif;
    font-weight: 700;
    font-size: 20px;
    line-height: 1.2;
    text-transform: uppercase;
    letter-spacing: .06em;
    white-space: nowrap;
  }
  .brand-name { display: flex; flex-direction: column; }
  .brand-dot {
    width: 34px; height: 34px; border-radius: 50%;
    background: var(--teal);
    flex: none;
  }
  .brand-front { left: 30px; top: 92px; color: var(--ink); }
  .brand-back {
    left: 50%; top: 50%; transform: translate(-50%, -50%);
    color: var(--paper);
  }

  .contact {
    position: absolute;
    right: 26px; top: 34px;
    text-align: right;
    color: var(--text-light);
    font-size: 14px;
    line-height: 1.45;
  }
  .contact-name { color: var(--teal); font-size: 17px; font-weight: 700; font-family: "Montserrat", Arial, sans-serif; }
  .contact-title { font-size: 14px; margin-bottom: 2px; }
  .contact-rule { display: inline-block; width: 12px; height: 1px; background: var(--teal); margin: 4px 0 10px; }
  .contact-line { display: flex; justify-content: flex-end; align-items: center; gap: 8px; }
  .contact-line svg { width: 13px; height: 13px; flex: none; }

  .pattern-field {
    position: absolute; inset: 0;
    background: radial-gradient(ellipse at 80% 25%, #3a3a3c 0%, #232325 45%, var(--ink-deep) 80%);
  }
</style>
</head>
<body>

  <section class="card card-front" aria-label="Card front">
    <svg class="front-shape" viewBox="0 0 540 309" preserveAspectRatio="none" aria-hidden="true">
      <path d="M0,0 H338 C330,120 210,250 0,282 V309 H0 Z" fill="var(--teal)"/>
      <path d="M0,0 H332 C322,118 200,242 0,272 Z" fill="var(--paper)"/>
    </svg>

    <div class="brand brand-front">
      <span class="brand-dot"></span>
      <span class="brand-name"><span>Hearthshine</span><span>Crew</span></span>
    </div>

    <div class="contact">
      <div class="contact-name">Corin ter Haghe</div>
      <div class="contact-title">Owner</div>
      <span class="contact-rule"></span>
      <div class="contact-line">1300 482 916
        <svg viewBox="0 0 24 24"><path fill="var(--teal)" d="M6.6 10.8a15 15 0 0 0 6.6 6.6l2.2-2.2c.3-.3.7-.4 1-.2 1.1.4 2.3.6 3.6.6.6 0 1 .4 1 1V20c0 .6-.4 1-1 1A17 17 0 0 1 3 4c0-.6.4-1 1-1h3.5c.6 0 1 .4 1 1 0 1.3.2 2.5.6 3.6.1.3 0 .7-.2 1z"/></svg>
      </div>
      <div class="contact-line">info@hearthshinecrew.com.au
        <svg viewBox="0 0 24 24"><path fill="var(--teal)" d="M2 5h20v14H2z"/><path d="M2 5l10 8 10-8" fill="none" stroke="var(--ink)" stroke-width="2"/></svg>
      </div>
      <div class="contact-line">www.hearthshinecrew.com.au
        <svg viewBox="0 0 24 24"><circle cx="12" cy="12" r="10" fill="var(--teal)"/><path d="M2 12h20M12 2c3 3 3 17 0 20M12 2c-3 3-3 17 0 20" fill="none" stroke="var(--ink)" stroke-width="1.4"/></svg>
      </div>
    </div>
  </section>

  <section class="card card-back" aria-label="Card back">
    <div class="pattern-field" role="img" aria-label="Tonal repeating brand-mark pattern in dark greys"></div>
    <div class="brand brand-back">
      <span class="brand-dot"></span>
      <span class="brand-name"><span>Hearthshine</span><span>Crew</span></span>
    </div>
  </section>

</body>
</html>
```